Corvath Properties Business Card Design

We would now like to design business cards with the new Corvath Properties logo

Target Market(s)

Professional

Industry/Entity Type

Professional services

Contact Information for Business Card

Employee name, title, phone number, email address, corporate office address and logo.

Font styles to use
Sans Serif

Colors
0054AA
0677BA
7BADD7
CADEEF
E8F1F8

Requirements
Must have
• My logo
Should not have
• any other pictures or images besides my logo

```html
<!DOCTYPE html>
<html lang="en">
<head>
<meta charset="utf-8">
<title>Corvath Properties – Business Cards</title>
<link rel="stylesheet" href="https://fonts.googleapis.com/css2?family=Bebas+Neue&family=Arimo:wght@400&display=swap">
<style>
  :root {
    --page-bg: #111213;
    --card-bg: #2a2b2d;
    --card-bg-deep: #232426;
    --emboss: #34363a;
    --brand-blue: #0677ba;
    --bright-blue: #1a86e8;
    --text-light: #d4d6d9;
    --text-muted: #b9bcc0;
  }
  * { box-sizing: border-box; margin: 0; padding: 0; }
  html, body { width: 1200px; height: 820px; overflow: hidden; }
  body {
    background: var(--page-bg);
    font-family: "Arimo", Arial, sans-serif;
    position: relative;
  }
  .card {
    position: absolute;
    top: 255px;
    width: 540px;
    height: 310px;
    background: var(--card-bg);
    border-bottom: 3px solid var(--bright-blue);
    overflow: hidden;
  }
  .card--front { left: 30px; border-left: 3px solid var(--bright-blue); }
  .card--back { left: 630px; background: var(--card-bg-deep); }

  /* Front */
  .brand {
    position: absolute;
    top: 40px;
    right: 40px;
    display: flex;
    align-items: center;
    gap: 14px;
  }
  .brand__square {
    width: 58px;
    height: 58px;
    background: var(--bright-blue);
  }
  .brand__name {
    font-family: "Bebas Neue", "Arial Narrow", sans-serif;
    font-size: 38px;
    line-height: 0.95;
    color: var(--bright-blue);
    letter-spacing: 1px;
  }
  .person {
    position: absolute;
    left: 40px;
    top: 142px;
  }
  .person__name {
    font-family: "Bebas Neue", "Arial Narrow", sans-serif;
    font-size: 30px;
    color: var(--bright-blue);
    line-height: 1;
  }
  .person__title {
    font-size: 15px;
    color: var(--text-light);
    margin-top: 2px;
  }
  .divider {
    position: absolute;
    left: 40px;
    right: 40px;
    top: 200px;
    height: 1px;
    background: var(--bright-blue);
  }
  .contacts {
    position: absolute;
    left: 40px;
    top: 214px;
    list-style: none;
  }
  .contacts__item {
    display: flex;
    align-items: center;
    gap: 9px;
    font-size: 15px;
    color: var(--text-light);
    height: 23px;
  }
  .contacts__item svg { width: 15px; height: 15px; fill: none; stroke: var(--bright-blue); stroke-width: 1.6; }
  .contacts__accent { color: var(--bright-blue); }
  .address {
    position: absolute;
    right: 40px;
    top: 214px;
    text-align: right;
    font-size: 14px;
    font-style: normal;
    line-height: 1.45;
    color: var(--text-muted);
  }

  /* Back */
  .back-mark {
    position: absolute;
    left: 40px;
    top: 50px;
    width: 210px;
    height: 210px;
    background: var(--emboss);
  }
  .back-name {
    position: absolute;
    left: 280px;
    top: 70px;
    font-family: "Bebas Neue", "Arial Narrow", sans-serif;
    font-size: 54px;
    line-height: 0.95;
    color: var(--bright-blue);
    letter-spacing: 2px;
  }
</style>
</head>
<body>
  <section class="card card--front" aria-label="Business card front">
    <div class="brand">
      <div class="brand__square"></div>
      <div class="brand__name">Corvath<br>Properties</div>
    </div>

    <div class="person">
      <p class="person__name">Elias Marlowe</p>
      <p class="person__title">Managing Director</p>
    </div>

    <div class="divider"></div>

    <ul class="contacts">
      <li class="contacts__item">
        <svg viewBox="0 0 16 16"><path d="M4 2 L6.5 5 L5 6.8 C6 9 7 10 9.2 11 L11 9.5 L14 12 L12.5 14 C7 14 2 9 2 3.5 Z"/></svg>
        044-555 018 273
      </li>
      <li class="contacts__item">
        <svg viewBox="0 0 16 16"><rect x="1.5" y="3.5" width="13" height="9"/><path d="M1.5 3.5 L8 9 L14.5 3.5"/></svg>
        info@corvathprops.com
      </li>
      <li class="contacts__item">
        <svg viewBox="0 0 16 16"><circle cx="8" cy="8" r="6.3"/><ellipse cx="8" cy="8" rx="2.8" ry="6.3"/><path d="M1.7 8 H14.3"/></svg>
        <span>www.<span class="contacts__accent">corvathprops</span>.com</span>
      </li>
    </ul>

    <address class="address">
      318, Harlow Street West<br>
      60217, Eastmere
    </address>
  </section>

  <section class="card card--back" aria-label="Business card back">
    <div class="back-mark"></div>
    <div class="back-name">Corvath<br>Properties</div>
  </section>
</body>
</html>
```